Ich bin Selfpublisher und suche immer mal wieder für meine Bücher schöne passende Cover
Es soll ansprechend sein, Titel muss gut lesbar sein, Untertitel auch. ich habe das Thema 'Wolkenlieder - Gärten der Stille' im Buch durch Tore/Türen die in eine jeweilige Welt führen abgebildet. Unten dazu einmal ein paar Beispiele die im Buch verwendet werden.
Das Cover soll möglichst hell sein, aber nicht zu weiss. Es muss ansprechend sein und den Leser Lust auf mehr machen :)
Das alte Titelcover ist mit dabei, aber es soll dann doch etwas anders werden..aber verträumt und friedlich, sanfte Farben ist schon eine gute Wahl.

```html
<!DOCTYPE html>
<html lang="de">
<head>
<meta charset="utf-8">
<title>Wolkenlieder – Gärten der Stille</title>
<link rel="stylesheet" href="https://fonts.googleapis.com/css2?family=Cinzel+Decorative:wght@400&family=Cinzel:wght@400&family=Marcellus&display=swap">
<style>
  :root {
    --page-bg: #d8d5d1;
    --sky-glow: #fffbf2;
    --sky-light: #faf3e6;
    --sky-warm: #efe0c6;
    --gold-cloud: #e2c9a0;
    --gold-deep: #c9a77c;
    --stair-light: #cfc2bb;
    --stair-mauve: #a48f86;
    --stair-deep: #7a6760;
    --title-silver: #45464b;
    --title-highlight: rgba(255, 255, 255, 0.9);
    --author-grey: #5c5c60;
    --subtitle-mauve: #7a6a6d;
  }
  html, body {
    margin: 0;
    padding: 0;
    width: 1200px;
    height: 1200px;
    overflow: hidden;
    background: var(--page-bg);
  }
  .book-cover {
    position: absolute;
    left: 209px;
    top: 0;
    width: 782px;
    height: 1200px;
    overflow: hidden;
  }
  .cover-art {
    position: absolute;
    inset: 0;
    background:
      /* bright gate opening */
      radial-gradient(ellipse 34% 30% at 50% 52%, var(--sky-glow) 0%, rgba(255,251,242,0.85) 45%, rgba(255,251,242,0) 100%),
      /* light path down the middle */
      radial-gradient(ellipse 22% 40% at 50% 92%, rgba(207,194,187,0.9) 0%, rgba(207,194,187,0) 100%),
      /* golden cloud banks at the sides */
      radial-gradient(ellipse 26% 42% at 6% 68%, var(--gold-cloud) 0%, rgba(226,201,160,0) 100%),
      radial-gradient(ellipse 26% 42% at 94% 68%, var(--gold-cloud) 0%, rgba(226,201,160,0) 100%),
      /* warm pillars in the upper sky */
      radial-gradient(ellipse 14% 40% at 18% 20%, rgba(239,214,170,0.8) 0%, rgba(239,214,170,0) 100%),
      radial-gradient(ellipse 14% 40% at 82% 20%, rgba(239,214,170,0.8) 0%, rgba(239,214,170,0) 100%),
      /* darker stair edges */
      linear-gradient(90deg, rgba(122,103,96,0.55) 0%, rgba(122,103,96,0) 30%, rgba(122,103,96,0) 70%, rgba(122,103,96,0.55) 100%),
      linear-gradient(180deg,
        var(--sky-warm) 0%,
        var(--sky-light) 28%,
        var(--sky-light) 50%,
        var(--gold-deep) 68%,
        var(--stair-mauve) 84%,
        var(--stair-deep) 100%);
  }
  .author {
    position: absolute;
    top: 62px;
    left: 0;
    right: 0;
    margin: 0;
    text-align: center;
    font-family: "Cinzel", serif;
    font-size: 36px;
    letter-spacing: 3px;
    color: var(--author-grey);
  }
  .title {
    position: absolute;
    top: 170px;
    left: 0;
    right: 0;
    margin: 0;
    text-align: center;
    font-family: "Cinzel Decorative", serif;
    font-weight: 400;
    font-size: 140px;
    line-height: 200px;
    color: var(--title-silver);
    text-shadow: 0 2px 0 var(--title-highlight), 0 0 8px rgba(255,255,255,0.7);
  }
  .title span { display: block; }
  .subtitle {
    position: absolute;
    top: 612px;
    left: 0;
    right: 0;
    margin: 0;
    text-align: center;
    font-family: "Marcellus", serif;
    font-weight: 400;
    font-size: 72px;
    line-height: 66px;
    color: var(--subtitle-mauve);
  }
  .subtitle span { display: block; }
</style>
</head>
<body>
  <main class="book-cover">
    <div class="cover-art" role="img" aria-label="Verträumte Illustration: breite helle Treppe zwischen Säulen und goldenen Wolkenblüten führt hinauf zu einem leuchtenden Himmelstor"></div>
    <p class="author">LENA MORGENTHAL</p>
    <h1 class="title"><span>WOLKEN</span><span>LIEDER</span></h1>
    <h2 class="subtitle"><span>Gärten</span><span>der</span><span>Stille</span></h2>
  </main>
</body>
</html>
```